Simple Clean Distinctive Fleet Graphic

Need design that can be used on truck (new Halvik Strider), and small/large cargo vans (new full size Halvik Porter, small size porter mini). Needs to include company logo, phone (555-314-9072) and “Service, Repair, Remodel” as the main focal point. Needs to also include “(Contractors License) or (CL) 58216,” which is a state requirement but not part of main focal point, just on bottom or off to the side in 2” letters/number.

Target Market(s)

Our core business is resort hotels, HOA's, and high end residential service and remodel projects.

Font styles to use
Sans Serif
Other font styles liked:
• logo is "what time is it" font

```html
<!DOCTYPE html>
<html lang="en">
<head>
<meta charset="utf-8">
<title>Aquaridge Fleet Graphic</title>
<link rel="stylesheet" href="https://fonts.googleapis.com/css2?family=Roboto+Condensed:wght@400;700&display=swap">
<style>
  :root {
    --paper: #ffffff;
    --panel: #f7f8f9;
    --panel-edge: #d9dde1;
    --ink: #1c1c1e;
    --band-dark: #1e1f22;
    --brand-blue: #3b8fcf;
    --deep-blue: #1d5f9e;
    --mid-blue: #2f7cc0;
    --light: #ffffff;
  }
  html, body {
    margin: 0;
    padding: 0;
    width: 1200px;
    height: 1200px;
    overflow: hidden;
    background: var(--paper);
  }
  .fleet-sheet {
    display: block;
    width: 1200px;
    height: 1200px;
  }
  .wrap-panel { fill: var(--panel); stroke: var(--panel-edge); stroke-width: 2; }
  .band-dark { fill: var(--band-dark); }
  .band-blue { fill: var(--mid-blue); }
  .band-deep { fill: var(--deep-blue); }
  .brand-name {
    font-family: "Roboto Condensed", sans-serif;
    font-weight: 400;
    fill: var(--brand-blue);
    letter-spacing: 1px;
  }
  .brand-mark { fill: var(--brand-blue); }
  .tagline {
    font-family: "Roboto Condensed", sans-serif;
    font-weight: 700;
    letter-spacing: 4px;
  }
  .tagline-light { fill: var(--light); }
  .tagline-dark { fill: var(--ink); }
  .phone {
    font-family: "Roboto Condensed", sans-serif;
    font-weight: 700;
    fill: var(--light);
    letter-spacing: 2px;
  }
  .web {
    font-family: "Roboto Condensed", sans-serif;
    font-weight: 700;
    fill: var(--light);
    letter-spacing: 1px;
  }
  .license {
    font-family: "Roboto Condensed", sans-serif;
    font-weight: 700;
    letter-spacing: 2px;
  }
  .license-dark { fill: var(--ink); }
  .license-light { fill: var(--light); }
  .dot { fill: var(--brand-blue); }
</style>
</head>
<body>
<svg class="fleet-sheet" viewBox="0 0 1200 1200" xmlns="http://www.w3.org/2000/svg">

  <!-- Pickup side layout -->
  <g class="layout-pickup">
    <rect class="wrap-panel" x="70" y="170" width="1060" height="300" rx="14"/>
    <text class="license license-dark" x="190" y="295" font-size="17">CL58216</text>

    <!-- rear blue sweep -->
    <path class="band-blue" d="M560 430 L760 300 L1130 270 L1130 410 L560 430 Z"/>
    <!-- rear top dark band -->
    <path class="band-dark" d="M790 298 L850 222 L1130 222 L1130 270 L930 288 Z"/>
    <!-- lower dark band -->
    <path class="band-dark" d="M340 410 L380 370 L700 370 L650 410 Z"/>
    <path class="band-deep" d="M340 418 L650 418 L700 410 L1130 410 L1130 424 L340 426 Z"/>

    <rect class="brand-mark" x="362" y="296" width="26" height="26"/>
    <text class="brand-name" x="400" y="335" font-size="62">aquaridge</text>

    <text class="tagline tagline-light" x="392" y="398" font-size="20">BUILD <tspan class="dot">•</tspan> SERVICE <tspan class="dot">•</tspan> REMODEL</text>
    <text class="phone" x="1068" y="260" font-size="30" text-anchor="end">555-314-9072</text>
    <text class="web" x="1068" y="285" font-size="16" text-anchor="end">www.aquaridgeLV.com</text>
  </g>

  <!-- Cargo van side layout -->
  <g class="layout-van">
    <rect class="wrap-panel" x="60" y="640" width="1080" height="380" rx="14"/>

    <rect class="brand-mark" x="470" y="718" width="34" height="34"/>
    <text class="brand-name" x="520" y="768" font-size="92">aquaridge</text>
    <text class="tagline tagline-dark" x="620" y="822" font-size="23" text-anchor="middle">BUILD <tspan class="dot">•</tspan> SERVICE <tspan class="dot">•</tspan> REMODEL</text>

    <!-- contact band -->
    <path class="band-dark" d="M450 880 L500 838 L1080 838 L1080 866 L1040 866 L1040 880 Z"/>
    <text class="phone" x="530" y="870" font-size="27">555-314-9072</text>
    <rect x="733" y="848" width="3" height="24" fill="var(--brand-blue)"/>
    <text class="web" x="752" y="869" font-size="22">www.aquaridgeLV.com</text>

    <!-- blue band -->
    <path class="band-blue" d="M430 900 L450 880 L1040 880 L1040 866 L1130 866 L1130 925 L430 925 Z"/>
    <text class="license license-light" x="1112" y="899" font-size="17" text-anchor="end">CL58216</text>

    <!-- lower skirt -->
    <rect class="band-dark" x="60" y="925" width="1080" height="60"/>
    <rect class="band-blue" x="330" y="960" width="780" height="10"/>
  </g>
</svg>
</body>
</html>
```